Square graphic for social media post

I want to create a 1080 x 1080px all-black image for the quote below that I can share on social media. I want the emphasis to be primarily on the quote, secondarily on the portrait, and third (smallest) on the logo. I want the background on the portrait to be edited so it's transparent and just shows the face of the person on a black background (no brick wall visible).

Graphic color: black
Text color: white
Content: "What we went through is going to make the greatest generation of hoteliers our industry has ever seen." << biggest text
Derek Holloway << smaller text
President, Ridgemont Hotels << smaller text
[image of person - use whichever version looks better to you]
[Add Lodging Ledger logo - whichever looks better to you]

This image needs to be readable when sized down much smaller (400x400?) so want the text and portrait to take up most of the space.

I'd like the output both as PNG and original file (preferably Canva). Thanks!

Target Market(s)

Hotel managers

Industry/Entity Type

Hospitality

Font styles to use
Sans Serif

Colors

Designer to choose colors to be used in the design.

Requirements
Must have
• Needs to focus on the quote and the person quoted (the portrait)

```html
<!DOCTYPE html>
<html lang="en">
<head>
<meta charset="utf-8">
<title>Quote Post – Derek Holloway</title>
<link href="https://fonts.googleapis.com/css2?family=Anton&family=Montserrat:wght@500&family=Open+Sans:wght@400;600;700&display=swap" rel="stylesheet">
<style>
  :root {
    --bg: #0a0a0b;
    --ink: #ffffff;
    --quote-mark-bg: #1c1c1e;
    --quote-mark-ink: #050505;
    --portrait-light: #d9d6d2;
    --portrait-mid: #a8988a;
    --portrait-dark: #2a3f7a;
  }
  html, body {
    margin: 0;
    padding: 0;
    width: 1200px;
    height: 1200px;
    overflow: hidden;
    background: var(--bg);
  }
  .post {
    position: relative;
    width: 1200px;
    height: 1200px;
    background: var(--bg);
    color: var(--ink);
    overflow: hidden;
  }
  .quote-mark {
    position: absolute;
    width: 82px;
    height: 82px;
  }
  .quote-mark--open { left: 75px; top: 72px; }
  .quote-mark--close { left: 535px; top: 845px; }

  .quote {
    position: absolute;
    left: 119px;
    top: 122px;
    margin: 0;
    font-family: "Anton", "Impact", sans-serif;
    font-weight: 400;
    font-size: 112px;
    line-height: 106px;
    text-transform: uppercase;
    letter-spacing: 0.005em;
  }
  .quote span { display: block; white-space: nowrap; }

  .portrait {
    position: absolute;
    left: 791px;
    top: 725px;
    width: 286px;
    height: 286px;
  }

  .attribution-line {
    position: absolute;
    left: 542px;
    top: 990px;
    width: 380px;
    height: 24px;
  }

  .speaker-name {
    position: absolute;
    left: 553px;
    top: 1030px;
    margin: 0;
    font-family: "Montserrat", "Helvetica", sans-serif;
    font-weight: 500;
    font-size: 34px;
    letter-spacing: -0.03em;
    line-height: 56px;
    text-transform: uppercase;
    white-space: nowrap;
  }
  .speaker-role {
    position: absolute;
    left: 892px;
    top: 1031px;
    margin: 0;
    font-family: "Open Sans", "Helvetica", sans-serif;
    line-height: 1.1;
  }
  .speaker-role__title {
    display: block;
    font-weight: 700;
    font-size: 26px;
  }
  .speaker-role__company {
    display: block;
    font-weight: 400;
    font-size: 18px;
  }

  .brand {
    position: absolute;
    left: 130px;
    top: 1040px;
    width: 330px;
    text-align: center;
    font-family: "Open Sans", "Helvetica", sans-serif;
    font-weight: 600;
    font-size: 22px;
    letter-spacing: 0.3em;
    text-transform: uppercase;
    white-space: nowrap;
  }
</style>
</head>
<body>
<main class="post">
  <svg class="quote-mark quote-mark--open" viewBox="0 0 82 82" aria-hidden="true">
    <circle cx="41" cy="41" r="41" fill="var(--quote-mark-bg)"/>
    <text x="41" y="68" text-anchor="middle" font-family="Georgia, serif" font-size="64" font-weight="700" fill="var(--quote-mark-ink)">&#8220;</text>
  </svg>

  <blockquote class="quote">
    <span>What we went</span>
    <span>through is</span>
    <span>going to make the</span>
    <span>greatest generation</span>
    <span>of hoteliers our</span>
    <span>industry has</span>
    <span>ever seen</span>
  </blockquote>

  <svg class="quote-mark quote-mark--close" viewBox="0 0 82 82" aria-hidden="true">
    <circle cx="41" cy="41" r="41" fill="var(--quote-mark-bg)"/>
    <text x="41" y="68" text-anchor="middle" font-family="Georgia, serif" font-size="64" font-weight="700" fill="var(--quote-mark-ink)">&#8221;</text>
  </svg>

  <svg class="portrait" viewBox="0 0 286 286" role="img" aria-label="Circular headshot portrait of Derek Holloway, smiling, in a navy blazer and white shirt">
    <defs>
      <linearGradient id="portraitFill" x1="0" y1="0" x2="0" y2="1">
        <stop offset="0" stop-color="var(--portrait-light)"/>
        <stop offset="0.55" stop-color="var(--portrait-mid)"/>
        <stop offset="1" stop-color="var(--portrait-dark)"/>
      </linearGradient>
    </defs>
    <circle cx="143" cy="143" r="140" fill="var(--ink)"/>
    <circle cx="143" cy="143" r="132" fill="url(#portraitFill)"/>
  </svg>

  <svg class="attribution-line" viewBox="0 0 380 24" aria-hidden="true">
    <line x1="12" y1="12" x2="375" y2="12" stroke="var(--ink)" stroke-width="4"/>
    <circle cx="12" cy="12" r="8" fill="var(--bg)" stroke="var(--ink)" stroke-width="4"/>
  </svg>

  <p class="speaker-name">Derek Holloway</p>
  <p class="speaker-role">
    <span class="speaker-role__title">President</span>
    <span class="speaker-role__company">Ridgemont Hotels</span>
  </p>

  <div class="brand">Lodging Ledger</div>
</main>
</body>
</html>
```